Global issue - challenge, change, create

Need a RESEARCH POSTER Based on Varenko challenge 2050, air pollution, effects, health issues, climate change, solutions to problems. Poster No longer than 100 cm x 100 cm. Eye catching poster. Eye catching topic, best pictorial presentation. no long paragraphs.
http://www.varenko-world.example/sustainability/environment/challenge2050/

Target Market(s)

students, teachers, public

Font styles to use
Serif
Decorative

Colors

Designer to choose colors to be used in the design.

Requirements
Must have
• need valuable datas, picture presentation, research poster style and format
Nice to have
• eye catching title, best pictorial, simple, nice color combination
Should not have
• No lengthy paragraph

```html
<!DOCTYPE html>
<html lang="en">
<head>
<meta charset="utf-8">
<title>Let's Put the Climate Back on the Healthier</title>
<link href="https://fonts.googleapis.com/css2?family=Amatic+SC:wght@400&family=Anton&family=Black+Ops+One&family=Open+Sans:wght@300;400&family=Oswald:wght@600&family=Francois+One&family=Stardos+Stencil:wght@700&display=swap" rel="stylesheet">
<style>
:root{
  --green:#3cb034;
  --green-dark:#2f6f1e;
  --red:#e31b23;
  --blue:#2196f3;
  --orange:#f7b63c;
  --ink:#1c1c1c;
  --grey:#555;
  --white:#fff;
}
*{margin:0;padding:0;box-sizing:border-box}
html,body{width:1200px;height:1200px;overflow:hidden;background:var(--white)}
.poster{position:relative;width:1200px;height:1200px;overflow:hidden;font-family:"Open Sans",sans-serif;color:var(--ink)}
.abs{position:absolute}
.art{position:absolute;z-index:0}
.txt{position:absolute;z-index:3;white-space:nowrap}
.rules{position:absolute;left:0;top:0;z-index:1}

.title-small{left:26px;top:22px;font-family:"Amatic SC",sans-serif;font-size:54px;line-height:1;color:var(--ink)}
.title-big{left:26px;top:82px;font-family:"Anton",sans-serif;font-size:56px;line-height:1;letter-spacing:1px;color:var(--ink)}

.body{font-size:27px;line-height:1.45;color:var(--ink)}
.stat-red{font-family:"Black Ops One",sans-serif;font-size:68px;color:var(--red);line-height:1}
.stat-top{font-family:"Stardos Stencil",sans-serif;font-weight:700;font-size:54px;color:var(--grey);line-height:1}
.stat-blue{font-family:"Oswald",sans-serif;font-weight:600;font-size:56px;color:var(--blue);line-height:1}

.fuel-label{font-family:"Black Ops One",sans-serif;font-size:25px;color:var(--orange);line-height:1}
.year{font-size:27px}
.chart-note{font-size:5px;font-weight:400;fill:#444;font-family:"Open Sans",sans-serif}

.climate-box{left:710px;top:550px;width:470px;height:175px;background:var(--green)}
.climate-text{left:828px;top:580px;font-size:26px;line-height:1.6;color:var(--white);font-weight:300}

.cost-head{left:20px;top:770px;font-size:52px;font-weight:300;color:var(--green);line-height:1}
.lives{left:860px;top:752px;font-family:"Black Ops One",sans-serif;font-size:92px;color:var(--ink);line-height:1;letter-spacing:1px}

.tip{font-family:"Francois One",sans-serif;line-height:1.4}
.tip-green{left:166px;top:828px;font-size:25px;color:var(--green)}
.tip-white{left:110px;top:1118px;font-size:22px;color:var(--white);text-align:center}
.tip-red{left:828px;top:938px;font-size:25px;color:var(--red)}
.tip-black{left:610px;top:1064px;width:590px;font-size:32px;color:var(--ink);text-align:center}
.tip-vertical{left:552px;top:1200px;font-family:"Francois One",sans-serif;font-size:20px;color:var(--white);transform:rotate(-90deg);transform-origin:0 0}
</style>
</head>
<body>
<main class="poster">

  <!-- Title -->
  <svg class="abs" style="left:0;top:0;z-index:1" width="640" height="176" viewBox="0 0 640 176">
    <polygon points="6,6 586,6 628,88 586,170 6,170" fill="none" stroke="var(--green)" stroke-width="8"/>
  </svg>
  <div class="txt title-small">LET'S PUT THE CLIMATE</div>
  <div class="txt title-big">BACK ON THE HEALTHIER</div>
  <div class="art" role="img" aria-label="Dark globe linked by a light bulb to a green globe" style="left:665px;top:15px;width:470px;height:130px;background:radial-gradient(circle at 15% 50%,#1b2b3a 0 55px,transparent 56px),radial-gradient(circle at 50% 50%,#1aa3b3 0 36px,transparent 37px),radial-gradient(circle at 86% 50%,#2f7db3 0 58px,transparent 59px),linear-gradient(#fff,#eef6fb)"></div>

  <!-- Divider rules -->
  <svg class="rules" width="1200" height="760" viewBox="0 0 1200 760">
    <g fill="none" stroke="var(--green)" stroke-width="4">
      <line x1="20" y1="210" x2="1180" y2="210"/>
      <line x1="20" y1="396" x2="1180" y2="396"/>
      <line x1="20" y1="535" x2="1180" y2="535"/>
      <line x1="20" y1="737" x2="1180" y2="737"/>
      <path d="M12 198 a12 12 0 0 1 0 24"/><path d="M1188 198 a12 12 0 0 0 0 24"/>
      <path d="M12 384 a12 12 0 0 1 0 24"/><path d="M1188 384 a12 12 0 0 0 0 24"/>
      <path d="M12 523 a12 12 0 0 1 0 24"/><path d="M1188 523 a12 12 0 0 0 0 24"/>
      <path d="M12 725 a12 12 0 0 1 0 24"/><path d="M1188 725 a12 12 0 0 0 0 24"/>
    </g>
    <line x1="644" y1="225" x2="644" y2="412" stroke="#7ccf57" stroke-width="3" stroke-dasharray="2 5"/>
  </svg>

  <!-- Row 1 -->
  <div class="art" role="img" aria-label="Broken red heart with a medical cross" style="left:4px;top:255px;width:102px;height:112px;background:linear-gradient(135deg,#e8222a,#b8141a);border-radius:40% 40% 50% 50%"></div>
  <div class="txt body" style="left:116px;top:252px">In 2010</div>
  <div class="txt stat-red" style="left:243px;top:228px">2.3 milion</div>
  <div class="txt body" style="left:116px;top:296px">deathsworld wide&nbsp; resulted from<br>air pollution</div>

  <div class="txt body" style="left:650px;top:238px;width:210px;text-align:right;line-height:1.48">Outdoor air<br>pollution ranks<br>in the</div>
  <div class="art" role="img" aria-label="Soft blue smoke swirl" style="left:868px;top:225px;width:190px;height:125px;background:radial-gradient(ellipse at center,#cfe6fb,rgba(255,255,255,0) 70%)"></div>
  <div class="txt stat-top" style="left:880px;top:262px">TOP10</div>
  <div class="txt body" style="left:1064px;top:248px;line-height:1.48">kilers<br>on esrth</div>

  <!-- Row 2 -->
  <div class="txt body" style="left:51px;top:412px;line-height:1.85">Breathng air in polluted metropolitan<br>areas redce your life expectancy</div>
  <div class="txt stat-blue" style="left:490px;top:452px">by 2 to 3 years.</div>
  <div class="art" role="img" aria-label="Smoking cars, truck, tractor and cargo ship" style="left:865px;top:402px;width:155px;height:118px;background:linear-gradient(#c9c9c9,#d6eef8 55%,#7cc4e2)"></div>

  <!-- Row 3: fuel sources -->
  <div class="txt fuel-label" style="left:46px;top:590px">FUEL</div>
  <div class="txt fuel-label" style="left:46px;top:656px">SOURCE</div>

  <svg class="abs" style="left:160px;top:548px;z-index:1" width="190" height="180" viewBox="0 0 190 180">
    <g transform="translate(88,88) rotate(-90)" fill="none" stroke-width="31">
      <circle r="55" stroke="#f8ee4a" stroke-dasharray="107.1 345.6" stroke-dashoffset="0"/>
      <circle r="55" stroke="#c6ea5e" stroke-dasharray="103.7 345.6" stroke-dashoffset="-107.1"/>
      <circle r="55" stroke="#8ddc7a" stroke-dasharray="69.1 345.6" stroke-dashoffset="-210.8"/>
      <circle r="55" stroke="#4fcd8a" stroke-dasharray="31.1 345.6" stroke-dashoffset="-279.9"/>
      <circle r="55" stroke="#21b496" stroke-dasharray="27.6 345.6" stroke-dashoffset="-311"/>
      <circle r="55" stroke="#128a84" stroke-dasharray="6.9 345.6" stroke-dashoffset="-338.7"/>
    </g>
    <text class="chart-note" x="44" y="13">CONVENTIOAL</text><text class="chart-note" x="48" y="19">8%</text>
    <text class="chart-note" x="95" y="7">OTHER</text><text class="chart-note" x="99" y="13">2%</text>
    <text class="chart-note" x="8" y="34">RENEVABLES</text><text class="chart-note" x="12" y="40">9%</text>
    <text class="chart-note" x="152" y="42">GAS</text><text class="chart-note" x="152" y="48">31%</text>
    <text class="chart-note" x="0" y="112">NUCLEAR</text><text class="chart-note" x="2" y="118">20%</text>
    <text class="chart-note" x="102" y="166">COAL</text><text class="chart-note" x="104" y="172">30%</text>
  </svg>
  <div class="art" role="img" aria-label="Fuel canister with oil drop" style="left:393px;top:578px;width:85px;height:102px;background:#1d1d1d;border-radius:12px"></div>
  <svg class="abs" style="left:516px;top:552px;z-index:1" width="190" height="180" viewBox="0 0 190 180">
    <g transform="translate(128,88) rotate(-90)" fill="none" stroke-width="31">
      <circle r="55" stroke="#f8ee4a" stroke-dasharray="76 345.6" stroke-dashoffset="0"/>
      <circle r="55" stroke="#c6ea5e" stroke-dasharray="152.1 345.6" stroke-dashoffset="-76"/>
      <circle r="55" stroke="#8ddc7a" stroke-dasharray="69.1 345.6" stroke-dashoffset="-228.1"/>
      <circle r="55" stroke="#4fcd8a" stroke-dasharray="17.3 345.6" stroke-dashoffset="-297.2"/>
      <circle r="55" stroke="#21b496" stroke-dasharray="24.2 345.6" stroke-dashoffset="-314.5"/>
      <circle r="55" stroke="#128a84" stroke-dasharray="6.9 345.6" stroke-dashoffset="-338.7"/>
    </g>
    <text class="chart-note" x="24" y="14">CONVENTIOAL</text><text class="chart-note" x="34" y="20">7%</text>
    <text class="chart-note" x="64" y="9">OTHER</text><text class="chart-note" x="68" y="15">2%</text>
    <text class="chart-note" x="2" y="30">RENEVABLES</text><text class="chart-note" x="12" y="36">5%</text>
    <text class="chart-note" x="175" y="28">GAS</text><text class="chart-note" x="175" y="34">22%</text>
    <text class="chart-note" x="10" y="88">NUCLEAR</text><text class="chart-note" x="14" y="94">20%</text>
    <text class="chart-note" x="130" y="166">COAL</text><text class="chart-note" x="132" y="172">44%</text>
  </svg>
  <div class="txt year body" style="left:297px;top:690px">2010 year</div>
  <div class="txt year body" style="left:467px;top:690px">2015 year</div>

  <div class="abs climate-box"></div>
  <div class="art" role="img" aria-label="Thermometer beside a heated globe" style="left:722px;top:556px;width:100px;height:165px;z-index:1;background:linear-gradient(90deg,#c7d2d8 0 22%,transparent 22%),radial-gradient(circle at 65% 62%,#2a7bb8 0 40px,transparent 41px)"></div>
  <div class="txt climate-text">Climates change is one<br>of the most greates<br>challenges of our time.</div>
  <div class="art" role="img" aria-label="Bare tree engulfed in flames" style="left:1112px;top:520px;width:88px;height:218px;z-index:1;background:linear-gradient(#3a2a1e 0 40%,#f08a1c 70%,#f5c33a)"></div>

  <!-- Row 4 -->
  <div class="txt cost-head">AIR POLLUTION COST MONEY AND</div>
  <div class="txt lives">LIVES</div>
  <div class="art" role="img" aria-label="Glossy red heart" style="left:1068px;top:822px;width:100px;height:80px;background:radial-gradient(circle at 40% 35%,#ff4a4a,#c00a0a);border-radius:45% 45% 50% 50%"></div>

  <div class="art" role="img" aria-label="Green recycling arrows" style="left:35px;top:822px;width:120px;height:118px;background:radial-gradient(circle,transparent 26px,#8cc63f 27px,#5aa02c 55px,transparent 56px)"></div>
  <div class="txt tip tip-green">Understand the concept of Reduce,<br>Reuse and Recycle</div>

  <div class="art" role="img" aria-label="Pine forest" style="left:0;top:910px;width:548px;height:290px;background:linear-gradient(#6f9a38,#2f5a14)"></div>
  <div class="txt tip tip-white">Conserve energy, Use energy efficient<br>devices, and safe your nature</div>

  <div class="art" role="img" aria-label="Two orange wind turbines" style="left:544px;top:830px;width:44px;height:370px;z-index:1;background:linear-gradient(#f7a93a,#f39200)"></div>
  <div class="txt tip-vertical">Emphasis on clean energy resources</div>

  <div class="art" role="img" aria-label="Splashing blue water" style="left:620px;top:860px;width:580px;height:340px;background:radial-gradient(ellipse at 55% 70%,#b9dcf5,rgba(255,255,255,0) 70%)"></div>
  <div class="art" role="img" aria-label="Red outline car with a green leaf" style="left:650px;top:892px;width:165px;height:125px;z-index:1;background:radial-gradient(ellipse at 55% 60%,rgba(227,27,35,.35),rgba(255,255,255,0) 65%),radial-gradient(ellipse at 8% 15%,#4cb82a 0 12px,transparent 13px)"></div>
  <div class="txt tip tip-red">Use public mode of transportation<br>or transport on natural gas.</div>
  <div class="txt tip tip-black">Each of our little shift planets helps a lot.<br>And we are a planet.</div>

</main>
</body>
</html>
```